Business Card Design

I want a simple and modern design, but also something very catching to the eye.

Also is there anyway that the text can be adjusted or changed so that I may make cards for other employees? If so, please make it so that I may edit the texts at a future date.

Reason: I need all designers to update the business card with my update information.

Industry/Entity Type

Business

Contact Information for Business Card

Owner: Marcus Halvorsen
Company Name: Play Brixo
Phone # :555-203-7841
Website: playbrixoshop.example
Email: marc@playbrixoshop.example

```html
<!DOCTYPE html>
<html lang="en">
<head>
<meta charset="utf-8">
<title>Play Brixo – Business Card</title>
<link rel="stylesheet" href="https://fonts.googleapis.com/css2?family=Montserrat:wght@300;400;600;700&display=swap">
<style>
  :root {
    --page-bg: #e9e6e1;
    --card-dark: #161616;
    --card-mid: #2c2c2c;
    --accent-blue: #1aa3d6;
    --accent-yellow: #ffd200;
    --accent-red: #e0261c;
    --text-light: #f2f2f2;
    --text-muted: #bdbdbd;
  }
  * { box-sizing: border-box; margin: 0; padding: 0; }
  html, body {
    width: 1200px;
    height: 900px;
    overflow: hidden;
    background: var(--page-bg);
    font-family: "Montserrat", "Century Gothic", sans-serif;
  }
  .stage {
    width: 1200px;
    height: 900px;
    display: flex;
    align-items: center;
    justify-content: center;
  }
  .business-card {
    position: relative;
    width: 1000px;
    height: 572px;
    border-radius: 34px;
    overflow: hidden;
    background: radial-gradient(ellipse at 50% 45%, var(--card-mid) 0%, var(--card-dark) 70%);
    box-shadow: 0 18px 40px rgba(0,0,0,0.25);
  }
  .card-holder {
    position: absolute;
    top: 58px;
    right: 62px;
    text-align: right;
  }
  .holder-name {
    font-size: 24px;
    letter-spacing: 1px;
    color: var(--accent-blue);
    text-transform: uppercase;
  }
  .holder-name .first { font-weight: 700; }
  .holder-name .last { font-weight: 300; }
  .holder-title {
    margin-top: 2px;
    margin-right: 70px;
    font-size: 21px;
    font-weight: 300;
    color: var(--text-muted);
  }
  .brand {
    position: absolute;
    top: 218px;
    left: 0;
    right: 0;
    display: flex;
    align-items: center;
    justify-content: center;
    gap: 22px;
  }
  .brand-mark {
    width: 78px;
    height: 78px;
    background: var(--accent-blue);
    border-radius: 8px;
  }
  .brand-name {
    font-size: 84px;
    font-weight: 700;
    color: var(--accent-yellow);
    letter-spacing: -1px;
  }
  .phone {
    position: absolute;
    top: 356px;
    right: 62px;
    font-size: 26px;
    font-weight: 600;
    letter-spacing: 1px;
    color: var(--text-light);
  }
  .contact-lines {
    position: absolute;
    left: 58px;
    bottom: 60px;
    color: var(--text-light);
    font-weight: 300;
  }
  .website {
    font-size: 24px;
    color: var(--text-muted);
    margin-bottom: 6px;
  }
  .email {
    font-size: 30px;
  }
  .color-band {
    position: absolute;
    left: 0;
    right: 0;
    bottom: 0;
    height: 24px;
    display: flex;
  }
  .color-band .band-yellow { flex: 0 0 36%; background: var(--accent-yellow); }
  .color-band .band-blue { flex: 0 0 36%; background: var(--accent-blue); }
  .color-band .band-red { flex: 1; background: var(--accent-red); }
</style>
</head>
<body>
  <main class="stage">
    <article class="business-card">
      <header class="card-holder">
        <p class="holder-name"><span class="first">Marcus</span> <span class="last">Halvorsen</span></p>
        <p class="holder-title">Owner</p>
      </header>

      <div class="brand">
        <span class="brand-mark" aria-hidden="true"></span>
        <span class="brand-name">Play Brixo</span>
      </div>

      <p class="phone">555-203-7841</p>

      <div class="contact-lines">
        <p class="website">playbrixoshop.example</p>
        <p class="email">marc@playbrixoshop.example</p>
      </div>

      <div class="color-band" aria-hidden="true">
        <span class="band-yellow"></span>
        <span class="band-blue"></span>
        <span class="band-red"></span>
      </div>
    </article>
  </main>
</body>
</html>
```